"Velmora Kestrel Bridgeworks": unique end to end Chinese marketing and ecommerce solutions*

I would like to create a company website for my trademark: "Velmora Kestrel Bridgeworks". We are based in Iceland. We are the only company in the market offering end-to-end Chinese digital marketing and eCommerce solutions. We help companies grow their brands and sales towards Chinese - whether tourism, export of products or services.
I include the logo that we have come up with in terms of colours and fonts.
The font is Trajan - I would like to use normal letters (capital and lowercase) for text.
Front page: Picture with colour filter. Logo in white. Text line underneath.
I am inspired by this website:
https://www.pelorumgrove.example/
I like these short videos for landing page:
https://www.framelodex.example/video/clip-30417852-ridge-scenic-vista-mountains
https://www.framelodex.example/video/clip-2093847155-4k-aerial-video-ridge-path-vista
https://www.framelodex.example/video/clip-3058172649-ridge-path-vista
Icelandic businesses looking for business opportunities in China or to attract Chinese tourists.
Digital Marketing

```html
<!DOCTYPE html>
<html lang="en">
<head>
<meta charset="utf-8">
<title>Velmora Kestrel Bridgeworks</title>
<link href="https://fonts.googleapis.com/css2?family=Catamaran:wght@700;800&family=Hind:wght@400;500;600&display=swap" rel="stylesheet">
<style>
:root{
  --blue:#0a4fa3;
  --gold:#b08a4a;
  --ink:#1b1b1b;
  --cream:#fdf5ec;
  --navy:#1c2b45;
  --field:#eef2f7;
  --white:#ffffff;
}
*{margin:0;padding:0;box-sizing:border-box}
html,body{width:1200px;height:4303px;overflow:hidden;background:var(--white)}
body{position:relative;font-family:'Hind',sans-serif;color:var(--ink)}
.abs{position:absolute}
.heading{font-family:'Catamaran',sans-serif;font-weight:800}
.btn{position:absolute;display:flex;align-items:center;justify-content:center;background:var(--blue);color:var(--white);font-size:15px;font-weight:500;border-radius:2px}
.btn-outline{position:absolute;display:flex;align-items:center;justify-content:center;gap:10px;border:2px solid var(--gold);color:var(--gold);font-size:15px;border-radius:2px;width:126px;height:37px}

/* hero */
.hero{left:0;top:0;width:1200px;height:632px;background:linear-gradient(180deg,#3e5d6c 0%,#5d6a55 45%,#4a4a36 75%,#3a3526 100%)}
.brand{color:var(--white);font-size:14px;font-weight:600;letter-spacing:.5px;line-height:1.2;display:flex;align-items:center;gap:8px}
.brand-dot{width:14px;height:14px;border-radius:50%;background:currentColor;flex:none}
.hero-title{left:0;width:1200px;top:172px;text-align:center;color:var(--white);font-size:70px;line-height:82px}
.hero-sub{left:0;width:1200px;top:344px;text-align:center;color:var(--white);font-size:28px;line-height:40px}

/* intro */
.intro-head{left:231px;top:736px;font-size:36px;line-height:40px}
.intro-head .blue{color:var(--blue)}.intro-head .gold{color:var(--gold)}
.intro-text{left:600px;top:736px;width:480px;font-size:25px;line-height:28px}

/* clients */
.clients{left:0;top:1043px;width:1200px;height:307px;background:var(--cream)}
.clients-title{left:0;width:1200px;top:1088px;text-align:center;font-size:23px;font-weight:600}
.client{position:absolute;top:1160px;width:147px;height:60px;background:var(--white);box-shadow:0 1px 4px rgba(0,0,0,.06);display:flex;align-items:center;justify-content:center;font-size:16px;font-weight:600;color:var(--blue);text-align:center;line-height:1.1}

/* services */
.photo{position:absolute;width:600px;height:400px}
.svc-title{font-size:62px;line-height:72px;color:var(--blue)}
.svc-text{font-size:17px;line-height:27px;width:290px}

/* contact */
.kicker{left:194px;top:3580px;color:var(--blue);font-size:25px;font-weight:600}
.contact-head{left:194px;top:3628px;font-size:27px;line-height:34px;font-weight:800}
.call{left:194px;top:3768px;color:var(--blue);font-size:17px}
.phone{left:194px;top:3802px;font-size:27px;font-weight:600}
.field{position:absolute;left:625px;width:380px;background:var(--field);border-bottom:2px solid var(--blue);color:#6b7280;font-size:15px;padding:10px 16px 0}

/* footer */
.footer{left:0;top:3980px;width:1200px;height:323px;background:var(--navy)}
.foot-text{left:240px;width:240px;top:4118px;text-align:center;color:var(--gold);font-size:16px;line-height:24px}
.foot-col h4{color:var(--white);font-size:15px;font-weight:600;margin-bottom:8px}
.foot-col p{color:var(--gold);font-size:14px;line-height:24.5px}
.foot-rule{left:0;top:4236px;width:1200px;height:1px;background:rgba(255,255,255,.15)}
.foot-small{top:4256px;color:var(--gold);font-size:12px}
</style>
</head>
<body>

<section class="abs hero" role="img" aria-label="Misty mountain ridge with an ancient wall winding over it under a muted colour filter"></section>
<div class="abs brand" style="left:72px;top:36px"><span class="brand-dot"></span>Velmora Kestrel<br>Bridgeworks</div>
<svg class="abs" style="left:1073px;top:36px" width="54" height="36" viewBox="0 0 54 36" aria-label="Menu"><g fill="#fff"><rect y="0" width="54" height="5" rx="2"/><rect y="15" width="54" height="5" rx="2"/><rect y="30" width="54" height="5" rx="2"/></g></svg>
<h1 class="abs heading hero-title">GROW YOUR BRAND<br>AND SALES IN CHINA.</h1>
<p class="abs hero-sub">We help companies and businesses expand<br>their presence in China</p>
<a class="btn" style="left:523px;top:441px;width:154px;height:43px">Get In Touch</a>

<h2 class="abs heading intro-head"><span class="blue">REAL PROBLEM</span><br><span class="gold">REAL RESULT</span></h2>
<a class="btn" style="left:239px;top:916px;width:132px;height:37px;font-size:14px">About us</a>
<p class="abs intro-text">We provide marketing and consulting services to startups, small businesses and large businesses looking to succeed in China. We work with you, not for you. Although we have great resources.<br><br>We are headquartered in China in order to best serve you.</p>

<section class="abs clients"></section>
<h3 class="abs clients-title">TRUSTED CLIENTS FROM 7 COUNTRIES</h3>
<div class="client" style="left:196px">Lornavale<br>Learning</div>
<div class="client" style="left:361px">Tessmar<br>Travel</div>
<div class="client" style="left:526px">Orvane<br>Games</div>
<div class="client" style="left:691px">Brantoke<br>Motors</div>
<div class="client" style="left:856px">Quellix<br>Web</div>
<a class="btn" style="left:523px;top:1263px;width:154px;height:38px;font-size:14px">Read Testimonial</a>

<!-- market research -->
<h2 class="abs heading svc-title" style="left:160px;top:1472px">MARKET<br>RESEARCH</h2>
<p class="abs svc-text" style="left:160px;top:1638px">We identify and analyze business opportunities in China.</p>
<a class="btn-outline" style="left:160px;top:1718px">Read More <svg width="18" height="10" viewBox="0 0 18 10"><path d="M0 5h16M12 1l4 4-4 4" fill="none" stroke="#b08a4a" stroke-width="1.6"/></svg></a>
<div class="photo" style="left:600px;top:1414px;background:linear-gradient(135deg,#c9d2da,#8ea3b8 55%,#5b6f88)" role="img" aria-label="Woman in a denim jacket checking her phone in a bright shopping mall"></div>

<!-- tourism -->
<div class="photo" style="left:0;top:1948px;background:linear-gradient(180deg,#b9c3c6,#7d8a87 55%,#4f5a52)" role="img" aria-label="Hiker on a steep stone wall path climbing a misty mountain"></div>
<h2 class="abs heading svc-title" style="left:719px;top:2022px">TOURISM</h2>
<p class="abs svc-text" style="left:719px;top:2117px">Lorem ipsum dolor sit amet, consetetur sadipscing elitr, sed diam nonumy eirmod tempor</p>
<a class="btn-outline" style="left:719px;top:2234px">Read More <svg width="18" height="10" viewBox="0 0 18 10"><path d="M0 5h16M12 1l4 4-4 4" fill="none" stroke="#b08a4a" stroke-width="1.6"/></svg></a>

<!-- digital marketing -->
<h2 class="abs heading svc-title" style="left:160px;top:2541px">DIGITAL<br>MARKETING</h2>
<p class="abs svc-text" style="left:160px;top:2705px">Lorem ipsum dolor sit amet, consetetur sadipscing elitr, sed</p>
<a class="btn-outline" style="left:160px;top:2787px">Read More <svg width="18" height="10" viewBox="0 0 18 10"><path d="M0 5h16M12 1l4 4-4 4" fill="none" stroke="#b08a4a" stroke-width="1.6"/></svg></a>
<div class="photo" style="left:600px;top:2483px;background:linear-gradient(160deg,#d7dccf,#9c8f76 45%,#8a4a3c 75%,#5b4b40)" role="img" aria-label="Busy pedestrian shopping street lined with shop signs"></div>

<!-- ecommerce -->
<div class="photo" style="left:0;top:3016px;background:linear-gradient(135deg,#3a4150,#6f7c86 45%,#c9c7b8 80%,#a6a28e)" role="img" aria-label="Woman browsing an online shopping site on a laptop"></div>
<h2 class="abs heading svc-title" style="left:719px;top:3054px">ECOMMERCE<br>SOLUTION</h2>
<p class="abs svc-text" style="left:719px;top:3220px">Lorem ipsum dolor sit amet, consetetur sadipscing elitr, sed diam nonumy eirmod tempor</p>
<a class="btn-outline" style="left:719px;top:3339px">Read More <svg width="18" height="10" viewBox="0 0 18 10"><path d="M0 5h16M12 1l4 4-4 4" fill="none" stroke="#b08a4a" stroke-width="1.6"/></svg></a>

<!-- contact -->
<p class="abs kicker">Get in touch</p>
<h3 class="abs heading contact-head">DON'T HESITATE TO<br>CONTACT US FOR FURTHER<br>INFORMATION</h3>
<p class="abs call">Call us for immediate consultation</p>
<p class="abs phone">+354 555 0182</p>
<div class="field" style="top:3584px;height:37px">Email Address</div>
<div class="field" style="top:3650px;height:37px">Subject</div>
<div class="field" style="top:3713px;height:114px">Your Message</div>
<a class="btn" style="left:625px;top:3857px;width:151px;height:36px">Send Message</a>

<!-- footer -->
<footer class="abs footer"></footer>
<div class="abs brand" style="left:290px;top:4050px;font-size:16px"><span class="brand-dot"></span>Velmora Kestrel<br>Bridgeworks</div>
<p class="abs foot-text">Lorem ipsum dolor sit amet, consetetur sadipscing elitr, sed diam nonumy eirmod.</p>
<div class="abs foot-col" style="left:582px;top:4028px"><h4>Our Services</h4><p>Market Research<br>Tourism<br>Digital Marketing<br>Ecommerce Solution</p></div>
<div class="abs foot-col" style="left:832px;top:4028px"><h4>Get Connected</h4><p>ChatLoom<br>ClipHarbor<br>ProTrellis<br>FriendPlaza</p></div>
<div class="abs foot-rule"></div>
<p class="abs foot-small" style="left:258px">Terms &amp; Conditions</p>
<p class="abs foot-small" style="left:388px">Privacy Policy</p>
<p class="abs foot-small" style="left:641px">© 2020 Velmora Kestrel Bridgeworks. All rights reserved.</p>

</body>
</html>
```